Etiketten-Design für Honig gesucht
Zielgruppe
Wir sind ein junges Unternehmen, welches sich auf die nachhaltige Vermarktung von Honig- und Honigprodukten spezialisiert. Neben verschiedenen Honigsorten, produzieren wir weitere Lebensmittel, wie z.B. Brotaufstriche, Süßwaren, Spirituosen, Getränke, Grillsaucen, Tee- und Gewürzmischungen, usw.
Unsere Zielgruppe sind ernährungsbewusste Menschen im jungen und mittleren Alter, welche ein nachhaltig-modernes Design mit Wiedererkennungswert anspricht. Unsere Produkte sind nicht für den täglichen Gebrauch gedacht, sondern mehr für den besonderen Moment. Daher auch qualitativ hochwertig und im höherpreisigen Segment zu finden. Auch als Geschenke/Mitbringsel bestens geeignet.
Wir suchen für unsere Honigproduktion ein dementsprechend geeignetes Etikettendesign.
Aufgabenstellung
Für uns ist es wichtig, nicht das Image des süßen kleinen Imkers aus der Nachbarschaft zu vermitteln.
Wir möchten auffallen, mit einem nachhaltig-modernen, frechen, kreativen und vor allem wiedererkennbaren Design.

```html
<!DOCTYPE html>
<html lang="de">
<head>
<meta charset="utf-8">
<title>Honig Etikett</title>
<link rel="stylesheet" href="https://fonts.googleapis.com/css2?family=Libre+Caslon+Text:wght@400&family=Open+Sans:wght@600;700&display=swap">
<style>
  :root {
    --backdrop: #eedbd0;
    --label-paper: #f7f6f4;
    --gold: #c9a24a;
    --gold-light: #e4cd8f;
    --honey-red: #8a1418;
    --subtitle-brown: #7a4a3e;
  }
  * { margin: 0; padding: 0; box-sizing: border-box; }
  html, body {
    width: 1200px;
    height: 1200px;
    overflow: hidden;
    background: var(--backdrop);
  }
  .canvas {
    width: 1200px;
    height: 1200px;
    display: flex;
    align-items: center;
    justify-content: center;
  }
  .label {
    position: relative;
    width: 980px;
    height: 620px;
    background: var(--label-paper);
    box-shadow: 0 10px 30px rgba(120, 70, 50, 0.12);
  }
  .rule {
    position: absolute;
    height: 2px;
    background: linear-gradient(90deg, var(--gold-light), var(--gold), var(--gold-light));
  }
  .rule--top-left { top: 128px; left: 0; width: 410px; }
  .rule--top-right { top: 128px; right: 0; width: 410px; }
  .rule--bottom { bottom: 40px; left: 0; width: 100%; }
  .crown {
    position: absolute;
    top: 90px;
    left: 50%;
    transform: translateX(-50%);
    width: 90px;
    height: 68px;
    border-radius: 6px;
    background: linear-gradient(180deg, #e8cf82, #b98d32);
  }
  .subtitle {
    position: absolute;
    top: 200px;
    width: 100%;
    text-align: center;
    font-family: "Open Sans", sans-serif;
    font-weight: 600;
    font-size: 30px;
    color: var(--subtitle-brown);
    letter-spacing: 0.5px;
  }
  .product-name {
    position: absolute;
    top: 240px;
    width: 100%;
    text-align: center;
    font-family: "Libre Caslon Text", serif;
    font-weight: 400;
    font-size: 138px;
    line-height: 1.2;
    color: var(--honey-red);
    letter-spacing: 6px;
  }
  .description {
    position: absolute;
    top: 420px;
    left: 150px;
    width: 680px;
    text-align: center;
    font-family: "Open Sans", sans-serif;
    font-weight: 700;
    font-size: 17px;
    line-height: 1.45;
    color: var(--honey-red);
  }
</style>
</head>
<body>
  <main class="canvas">
    <section class="label">
      <div class="rule rule--top-left"></div>
      <div class="crown" role="img" aria-label="Goldene Krone als Schmuckelement"></div>
      <div class="rule rule--top-right"></div>
      <p class="subtitle">nachhaltig produziert</p>
      <h1 class="product-name">HONEY</h1>
      <p class="description">Aus reinem Blütennektar schonend geschleudert und kalt abgefüllt. Ohne Zusätze, voller Aroma und mit Sorgfalt gewonnen – für besondere Momente, zum Verschenken und Genießen.</p>
      <div class="rule rule--bottom"></div>
    </section>
  </main>
</body>
</html>
```